App design for Monitoring/Notifying Patient's Medication

Design of UX for an Android App that helps patients with medications.

Patient should be able to interact with the App to inform that they have taken the medication (tablets and injections) at proper times.
Ability in App to notify the patient for taking medicines or injections at the proper times.
Medicines and injections to be taken multiple times a day.
Notifications can be visual and audio. Audio may include name and dosage info also.

App requirements
Ability for patient to interact with app to inform that medicine and/or injection has been taken.
Ability to show visual/audio notifications at scheduled times if patient has not taken medicine or injection.
Audio may contain name and dosage of medicine.
In order to increase the use of App, please suggest how to add a rewards section. High level intent is to reward patients who have been taking medications as prescribed for a month.
Menu button at the top which will have 3 action buttons:
1- Home : on click of which the user is back on the landing/notification page.
2-On click of which this will lead the user to a details screen where he can view his medication details as to what all medicines and injections he is taking along with the schedules and the next upcoming notification. This page is entirely read only. It may have a button to help the user go back to the landing page.
3-On click of which, this will show a history of his actions taken in the last 30 days, if the user has pushed the button on notification every time he has consumed the medicine. This page is entirely read only. It may have a button to help the user go back to the landing page.

Thus 3 screens have to be designed:
Home Page
Page for Menu Action button 2
Page for Menu Action button 3

The menu button should be available in all the 3 pages.

The app needs to be simple, friendly and lively so that it ignites an interest in the user to use the app. Please note that many users are illiterate.

It has to be designed only for android phones that will have around 5 inche screen with a resolution between 360 x 640 and 1280 x 720 pixels

Target Market(s)

Patients(most of them are illiterate

Industry/Entity Type

Healthcare

Requirements
Must have
• - best use of screen space. minimum click and scrolls.
• - clean and elegant look.
• - basic font styles
• - bright colors.

```html
<!DOCTYPE html>
<html lang="en">
<head>
<meta charset="utf-8">
<title>Today – Medication Tracker</title>
<link rel="stylesheet" href="https://fonts.googleapis.com/css2?family=Roboto:wght@400;500;700&display=swap">
<style>
:root{
  --bg:#efefef;
  --white:#ffffff;
  --ink:#2b2b2b;
  --muted:#444444;
  --blue:#3d9ad6;
  --amber:#f6c453;
  --amber-row:#f5c55b;
  --gold:#f3bb2f;
  --line:#e2e2e2;
  --nav-dark:#000000;
  --nav-accent:#2b3a8f;
  --thumb:#c9b8bd;
}
*{box-sizing:border-box;margin:0;padding:0}
html,body{width:1200px;height:2566px;overflow:hidden;background:var(--bg)}
body{font-family:"Roboto",Arial,sans-serif;color:var(--ink)}
.screen{position:absolute;left:0;top:0;width:375px;height:802px;transform:scale(3.2);transform-origin:0 0;background:var(--bg);overflow:hidden}
.status-bar{position:absolute;left:0;top:0;width:375px;height:24px;background:var(--white);font-size:11px;color:#555}
.status-bar .time{position:absolute;right:6px;top:5px}
.status-bar svg{position:absolute;right:38px;top:6px}
.app-header{position:absolute;left:0;top:24px;width:375px;height:48px;background:var(--white)}
.app-header h1{position:absolute;left:14px;top:12px;font-size:16px;font-weight:700}
.app-header .add{position:absolute;right:10px;top:10px}
.summary-card{position:absolute;left:8px;top:82px;width:358px;height:199px;background:var(--white);border-radius:4px;border:1px solid var(--line)}
.summary-card .divider-v{position:absolute;left:181px;top:0;width:1px;height:130px;background:var(--line)}
.summary-card .divider-h{position:absolute;left:0;top:130px;width:100%;height:1px;background:var(--line)}
.next-dose{position:absolute;left:17px;top:17px}
.next-dose .label{margin-top:8px;font-size:14px;color:var(--muted)}
.next-dose .value{font-size:23px;font-weight:700;margin-top:2px}
.streak{position:absolute;left:181px;top:14px;width:177px;text-align:center}
.streak .days{font-size:18px;font-weight:500;color:var(--blue);margin-top:2px}
.streak .label{font-size:13px;color:var(--muted);margin-top:3px}
.complete-btn{position:absolute;left:11px;top:143px;width:336px;height:44px;border-radius:22px;background:var(--amber);color:var(--white);font-size:16px;font-weight:700;display:flex;align-items:center;justify-content:center;gap:9px;box-shadow:0 2px 3px rgba(0,0,0,.15)}
.med-list{position:absolute;left:8px;top:295px;width:358px}
.med-row{position:relative;height:74px;margin-bottom:7px;background:var(--amber-row);border-radius:2px}
.med-row .name{position:absolute;left:16px;top:0;line-height:74px;font-size:17px;font-weight:700;color:var(--ink)}
.med-row .thumb{position:absolute;left:208px;top:4px;width:65px;height:65px;border:2px solid var(--white);border-radius:3px;background:linear-gradient(135deg,#e8dfe3,var(--thumb))}
.med-row .thumb.blue{background:linear-gradient(180deg,#ffffff 55%,#2a3e8c)}
.med-row .thumb.tabs{background:linear-gradient(135deg,#f4f1ee,#c6d0dc)}
.med-row .thumb.label{background:linear-gradient(135deg,#eef1e6,#c8ccb8)}
.med-row .dose{position:absolute;left:288px;top:0;width:68px;height:74px}
.bottom-nav{position:absolute;left:0;top:704px;width:375px;height:52px;background:var(--white);border-top:1px solid var(--line)}
.tab{position:absolute;top:7px;width:120px;text-align:center;font-size:11px;color:var(--muted)}
.tab svg{display:block;margin:0 auto 4px}
.tab.active{color:var(--blue)}
.system-nav{position:absolute;left:0;top:756px;width:375px;height:46px;background:var(--nav-dark);border-top:2px solid var(--nav-accent)}
.system-nav svg{position:absolute;left:0;top:0}
</style>
</head>
<body>
<div class="screen">
  <div class="status-bar">
    <svg width="60" height="12" viewBox="0 0 60 12">
      <circle cx="5" cy="6" r="4.5" fill="none" stroke="#666" stroke-width="1.2"/>
      <path d="M16 10 L22 3 L28 10 Z" fill="#666"/>
      <path d="M33 11 L43 1 L43 11 Z" fill="#666"/>
      <rect x="49" y="1" width="6" height="10" rx="1" fill="#666"/>
    </svg>
    <span class="time">16:54</span>
  </div>

  <header class="app-header">
    <h1>Today</h1>
    <svg class="add" width="22" height="22" viewBox="0 0 22 22">
      <circle cx="11" cy="11" r="10" fill="none" stroke="var(--blue)" stroke-width="1.8"/>
      <path d="M11 6v10M6 11h10" stroke="var(--blue)" stroke-width="1.8" stroke-linecap="round"/>
    </svg>
  </header>

  <section class="summary-card">
    <div class="next-dose">
      <svg width="40" height="40" viewBox="0 0 40 40">
        <circle cx="20" cy="20" r="17" fill="none" stroke="var(--gold)" stroke-width="3"/>
        <path d="M20 11v12" stroke="var(--gold)" stroke-width="3.4" stroke-linecap="round"/>
        <circle cx="20" cy="29" r="2" fill="var(--gold)"/>
      </svg>
      <p class="label">Next dose due</p>
      <p class="value">Due now</p>
    </div>
    <div class="divider-v"></div>
    <div class="streak">
      <svg width="40" height="40" viewBox="0 0 40 40">
        <path d="M11 4h18v12a9 9 0 0 1-18 0z" fill="var(--gold)"/>
        <path d="M11 8H5v4a7 7 0 0 0 7 7M29 8h6v4a7 7 0 0 1-7 7" fill="none" stroke="var(--gold)" stroke-width="2.5"/>
        <rect x="18" y="24" width="4" height="7" fill="var(--gold)"/>
        <rect x="12" y="31" width="16" height="5" rx="1" fill="var(--gold)"/>
        <text x="20" y="16" text-anchor="middle" font-size="10" font-family="Roboto,Arial,sans-serif" fill="#fff">7</text>
      </svg>
      <p class="days">7 Days</p>
      <p class="label">Complete</p>
    </div>
    <div class="divider-h"></div>
    <div class="complete-btn">
      <svg width="22" height="22" viewBox="0 0 22 22">
        <circle cx="11" cy="11" r="9.5" fill="none" stroke="#fff" stroke-width="1.8"/>
        <path d="M6.5 11.2l3 3 6-6.2" fill="none" stroke="#fff" stroke-width="1.8" stroke-linecap="round" stroke-linejoin="round"/>
      </svg>
      Complete dose
    </div>
  </section>

  <section class="med-list">
    <div class="med-row">
      <span class="name">Ethionamide</span>
      <div class="thumb" role="img" aria-label="Product photo of ethionamide vial and box"></div>
      <svg class="dose" viewBox="0 0 68 74">
        <rect x="12" y="30" width="20" height="12" rx="6" fill="#fff" transform="rotate(-35 22 36)"/>
        <rect x="42" y="30" width="20" height="12" rx="6" fill="#fff" transform="rotate(-35 52 36)"/>
      </svg>
    </div>
    <div class="med-row">
      <span class="name">Streptomysin 500</span>
      <div class="thumb blue" role="img" aria-label="Product photo of streptomycin injection box"></div>
      <svg class="dose" viewBox="0 0 68 74">
        <g transform="rotate(45 36 37)" fill="none" stroke="#fff" stroke-width="2.2" stroke-linecap="round">
          <rect x="31" y="26" width="10" height="20" rx="1"/>
          <path d="M36 46v9M36 20v6M31 20h10M33 31h3M33 36h3M33 41h3"/>
        </g>
      </svg>
    </div>
    <div class="med-row">
      <span class="name">Ethionamide</span>
      <div class="thumb" role="img" aria-label="Product photo of ethionamide vial and box"></div>
      <svg class="dose" viewBox="0 0 68 74">
        <rect x="12" y="30" width="20" height="12" rx="6" fill="#fff" transform="rotate(-35 22 36)"/>
        <rect x="42" y="30" width="20" height="12" rx="6" fill="#fff" transform="rotate(-35 52 36)"/>
      </svg>
    </div>
    <div class="med-row">
      <span class="name">Ofloxacin</span>
      <div class="thumb tabs" role="img" aria-label="Product photo of ofloxacin tablet strip and box"></div>
      <svg class="dose" viewBox="0 0 68 74">
        <rect x="30" y="16" width="20" height="12" rx="6" fill="#fff" transform="rotate(-35 40 22)"/>
        <rect x="14" y="42" width="20" height="12" rx="6" fill="#fff" transform="rotate(-35 24 48)"/>
        <rect x="44" y="42" width="20" height="12" rx="6" fill="#fff" transform="rotate(-35 54 48)"/>
      </svg>
    </div>
    <div class="med-row">
      <span class="name">Pyrazinamide</span>
      <div class="thumb label" role="img" aria-label="Product photo of pyrazinamide tablet box"></div>
      <svg class="dose" viewBox="0 0 68 74">
        <rect x="26" y="30" width="20" height="12" rx="6" fill="#fff" transform="rotate(-35 36 36)"/>
      </svg>
    </div>
  </section>

  <nav class="bottom-nav">
    <div class="tab active" style="left:-4px">
      <svg width="20" height="18" viewBox="0 0 20 18" fill="none" stroke="var(--blue)" stroke-width="1.6" stroke-linecap="round">
        <path d="M2 3l1.5 1.5L6 2M2 9l1.5 1.5L6 8M2 15l1.5 1.5L6 14M9 3.5h9M9 9.5h9M9 15.5h9"/>
      </svg>
      Today
    </div>
    <div class="tab" style="left:124px">
      <svg width="20" height="18" viewBox="0 0 20 18" fill="none" stroke="#777" stroke-width="1.6">
        <rect x="3" y="5" width="14" height="8" rx="4" transform="rotate(-40 10 9)"/>
        <path d="M7.5 5.5l5 6" />
      </svg>
      My Medication
    </div>
    <div class="tab" style="left:253px">
      <svg width="20" height="18" viewBox="0 0 20 18" fill="none" stroke="#777" stroke-width="1.5">
        <rect x="3" y="3" width="14" height="14" rx="1"/>
        <path d="M3 7h14M7 1v4M13 1v4M6 10h2M9 10h2M12 10h2M6 13h2M9 13h2M12 13h2"/>
      </svg>
      Schedule
    </div>
  </nav>

  <div class="system-nav">
    <svg width="375" height="44" viewBox="0 0 375 44" fill="none" stroke="#fff" stroke-width="2">
      <path d="M98 13 L80 22 L98 31 Z" stroke-linejoin="round"/>
      <circle cx="187" cy="22" r="10"/>
      <rect x="277" y="12" width="20" height="20" rx="1"/>
    </svg>
  </div>
</div>
</body>
</html>
```